Business Card Design for Technology Company

New business card design needed for technology company director.
Ideally, the design will fit the style and nature of the industry. We are a supplier of quality products and services, and we hope the design will give customers and suppliers this impression.

Target Market(s)

3D Printing Industry

Industry/Entity Type

Technology Equipment

Contact Information for Business Card

Name: Marcus Lyle
Title: Director
Company address: Factory K4, 7B Morland Road, Springvale Victoria Australia 3150
Telephone: +61-3-8555 6413
Email: marcus.lyle@veranox.com.au
Website: www.veranox.com.au

Requirements
Must have
• All information in business card details
• Company logo
• '3D Printers and 3D Print Filaments' at proper place
Nice to have
• Style to fit the industry
• Colour to fit logo

```html
<!DOCTYPE html>
<html lang="en">
<head>
<meta charset="utf-8">
<title>Veranox Technology – Business Card</title>
<link href="https://fonts.googleapis.com/css2?family=Montserrat:wght@400;500&family=Arimo:wght@400&family=Tinos:wght@400&display=swap" rel="stylesheet">
<style>
  :root {
    --page-bg: #e9e6ee;
    --card-deep: #120d1c;
    --card-mid: #1e1730;
    --card-glow: #2a2142;
    --groove-light: #2c2440;
    --groove-dark: #08060d;
    --ink-white: #f3f1f7;
    --ink-soft: #cfcadb;
    --accent: #f2b21b;
    --accent-blue: #2f8fd8;
  }
  * { margin: 0; padding: 0; box-sizing: border-box; }
  html, body { width: 1200px; height: 1200px; overflow: hidden; }
  body {
    background: var(--page-bg);
    display: flex; flex-direction: column; align-items: center; justify-content: center;
    gap: 52px;
  }
  .card {
    position: relative;
    width: 900px; height: 514px;
    border-radius: 6px;
    overflow: hidden;
    background:
      radial-gradient(ellipse 60% 70% at 45% 40%, var(--card-glow) 0%, transparent 70%),
      linear-gradient(160deg, var(--card-mid) 0%, var(--card-deep) 100%);
    box-shadow: 0 14px 34px rgba(20, 10, 40, .35);
  }
  .card__grooves { position: absolute; inset: 0; width: 100%; height: 100%; }

  .identity { position: absolute; left: 120px; top: 64px; }
  .identity__name {
    font-family: "Montserrat", sans-serif; font-weight: 400;
    font-size: 34px; letter-spacing: 1px; color: var(--ink-white);
    text-transform: uppercase; line-height: 1;
  }
  .identity__name .surname { font-size: 27px; text-transform: none; }
  .identity__title {
    font-family: "Tinos", serif; font-size: 11px; letter-spacing: 1.2px;
    color: var(--ink-soft); margin-top: 3px;
  }

  .contacts { position: absolute; left: 90px; top: 200px; list-style: none; }
  .contacts__item {
    display: flex; align-items: center; gap: 14px;
    font-family: "Arimo", sans-serif; font-size: 13.5px; color: var(--ink-soft);
    height: 34px;
  }
  .contacts__icon { width: 18px; height: 18px; flex: none; }

  .brand {
    position: absolute; display: flex; align-items: center; gap: 18px;
  }
  .brand__dot {
    width: 64px; height: 64px; border-radius: 50%;
    background: radial-gradient(circle at 40% 35%, #2a2340, #0c0914);
    box-shadow: inset 0 0 0 2px #0a0810, 0 0 0 1px #332a48;
  }
  .brand__text { display: flex; flex-direction: column; }
  .brand__name {
    font-family: "Montserrat", sans-serif; font-weight: 500;
    font-size: 30px; letter-spacing: 7px; color: var(--ink-white); line-height: 1;
  }
  .brand__sub {
    font-family: "Montserrat", sans-serif; font-weight: 500;
    font-size: 9px; letter-spacing: 6.5px; color: var(--ink-white); margin-top: 5px;
  }
  .card--front .brand { left: 588px; top: 262px; }
  .card--back .brand { left: 462px; top: 300px; }
</style>
</head>
<body>

<section class="card card--front" aria-label="Business card front">
  <svg class="card__grooves" viewBox="0 0 900 514" aria-hidden="true">
    <g fill="none" stroke-linecap="round">
      <path d="M620 294 L572 0" stroke="var(--groove-light)" stroke-width="14"/>
      <path d="M620 294 L572 0" stroke="var(--groove-dark)" stroke-width="2" transform="translate(-6 0)"/>
      <path d="M620 294 L400 514" stroke="var(--groove-light)" stroke-width="14"/>
      <path d="M620 294 L400 514" stroke="var(--groove-dark)" stroke-width="2" transform="translate(-5 -4)"/>
      <path d="M620 294 L900 330" stroke="var(--groove-light)" stroke-width="10" opacity=".5"/>
    </g>
  </svg>

  <div class="identity">
    <h1 class="identity__name">Marcus <span class="surname">Lyle</span></h1>
    <p class="identity__title">DIRECTOR</p>
  </div>

  <ul class="contacts">
    <li class="contacts__item">
      <svg class="contacts__icon" viewBox="0 0 18 18"><circle cx="9" cy="9" r="8" fill="none" stroke="var(--accent)" stroke-width="1.4"/><path d="M6 5.5c0 4 2.5 6.5 6.5 6.5l.5-1.6-1.8-.8-.8.9c-1.3-.5-2.3-1.5-2.8-2.8l.9-.8-.8-1.8z" fill="var(--accent)"/></svg>
      +61-3-8555 6413
    </li>
    <li class="contacts__item">
      <svg class="contacts__icon" viewBox="0 0 18 18"><circle cx="9" cy="9" r="8" fill="none" stroke="var(--accent)" stroke-width="1.4"/><path d="M5 9.2 13 5.5 10.5 13 9 10z" fill="var(--accent)"/></svg>
      marcus.lyle@veranox.com.au
    </li>
    <li class="contacts__item">
      <svg class="contacts__icon" viewBox="0 0 18 18"><circle cx="9" cy="9" r="8" fill="none" stroke="var(--accent)" stroke-width="1.4"/><path d="M5 9.2 13 5.5 10.5 13 9 10z" fill="var(--accent)"/></svg>
      www.veranox.com.au
    </li>
    <li class="contacts__item">
      <svg class="contacts__icon" viewBox="0 0 18 18"><circle cx="9" cy="9" r="8" fill="none" stroke="var(--accent)" stroke-width="1.4"/><path d="M9 4.5a3 3 0 0 0-3 3c0 2.2 3 5.5 3 5.5s3-3.3 3-5.5a3 3 0 0 0-3-3z" fill="var(--accent)"/><circle cx="9" cy="7.5" r="1" fill="var(--card-deep)"/></svg>
      Factory K4, 7B Morland Road, Springvale Victoria Australia 3150
    </li>
  </ul>

  <div class="brand">
    <span class="brand__dot"></span>
    <span class="brand__text">
      <span class="brand__name">VERANOX</span>
      <span class="brand__sub">TECHNOLOGY</span>
    </span>
  </div>
</section>

<section class="card card--back" aria-label="Business card back">
  <svg class="card__grooves" viewBox="0 0 900 514" aria-hidden="true">
    <g fill="none" stroke-linecap="round">
      <path d="M494 332 L560 0" stroke="var(--groove-light)" stroke-width="14"/>
      <path d="M494 332 L560 0" stroke="var(--groove-dark)" stroke-width="2" transform="translate(-6 0)"/>
      <path d="M494 332 L0 380" stroke="var(--groove-light)" stroke-width="14"/>
      <path d="M494 332 L0 380" stroke="var(--groove-dark)" stroke-width="2" transform="translate(0 -6)"/>
      <path d="M494 332 L330 514" stroke="var(--groove-light)" stroke-width="10" opacity=".5"/>
    </g>
  </svg>

  <div class="brand">
    <span class="brand__dot"></span>
    <span class="brand__text">
      <span class="brand__name">VERANOX</span>
      <span class="brand__sub">TECHNOLOGY</span>
    </span>
  </div>
</section>

</body>
</html>
```